We currently have a good logo and we want business cards that can display our logo but also represent our industry - telecom construction - We are a construction company specializing in telecom construction such as installation of fiber optic cable throughout cities and across the country. Nationwide services
We are large enough to handle most any project yet small enough to be a flexible partner and resource.

Target Market(s)

U.S. based telecom carriers and providers

Industry/Entity Type

Construction

Contact Information for Business Card

Business cards should include our logo, phone number and website address. Also, including some information as to our core services would be good.

Colors

Designer to choose colors to be used in the design.

Requirements
Must have
• Colors based on logo
• Must use our logo
• Logo, name, email, website address, phone number
• Tovek Subterra
• Brent Dacosta
• Director of Business Development
• (913) 555-0187
• www.tovekgrid.example
Nice to have
• Construction services including:
• Small Cell Construction
• Boring/Drilling
• Plowing / Trenching
• Conduit installation
• Fiber pulling
• splicing
• building entries
• Aerial construction
• Aerial Make Ready
• Make Ready Engineering
Should not have
• We are open to ideas

```html
<!DOCTYPE html>
<html lang="en">
<head>
<meta charset="utf-8">
<title>Tovek Subterra Business Card</title>
<link href="https://fonts.googleapis.com/css2?family=Montserrat:wght@400;500;600;700;800&display=swap" rel="stylesheet">
<style>
  :root {
    --page-bg: #ececec;
    --card-white: #f3f3f3;
    --brand-blue: #0d4fa8;
    --brand-deep: #074a98;
    --brand-bright: #1ea3d8;
    --text-grey: #555a60;
    --rule-grey: #8a8d91;
    --white: #ffffff;
  }
  * { box-sizing: border-box; margin: 0; padding: 0; }
  html, body { width: 1200px; height: 1200px; overflow: hidden; }
  body {
    background: var(--page-bg);
    font-family: "Montserrat", sans-serif;
    position: relative;
  }
  .card {
    position: absolute;
    left: 227px;
    width: 746px;
    height: 425px;
    text-align: center;
  }
  .card--front { top: 135px; background: var(--card-white); }
  .card--back {
    top: 640px;
    background: linear-gradient(180deg, var(--brand-deep) 0%, #1490cf 30%, var(--brand-bright) 50%, #1490cf 68%, var(--brand-deep) 100%);
    color: var(--white);
  }
  .wordmark {
    position: absolute;
    left: 0; right: 0;
    font-weight: 800;
    letter-spacing: 1px;
    line-height: 1;
  }
  .card--front .wordmark { top: 92px; font-size: 50px; color: var(--brand-blue); }
  .card--back .wordmark { top: 110px; font-size: 54px; color: var(--white); }
  .person-name {
    position: absolute; top: 274px; left: 0; right: 0;
    font-size: 22px; font-weight: 600; color: var(--brand-blue);
  }
  .title-row {
    position: absolute; top: 301px; left: 0; right: 0;
    display: flex; align-items: center; gap: 10px;
  }
  .title-row .rule { flex: 1; height: 1px; background: var(--rule-grey); }
  .job-title { font-size: 16px; color: var(--text-grey); white-space: nowrap; }
  .contact-row {
    position: absolute; top: 344px; left: 0; right: 0;
    display: flex; justify-content: center; align-items: center; gap: 6px;
    font-size: 16px; color: var(--text-grey);
  }
  .contact-row svg { width: 17px; height: 17px; }
  .contact-row .gap { width: 6px; }
  .website {
    position: absolute; top: 380px; left: 0; right: 0;
    font-size: 16px; color: var(--text-grey);
  }
  .website strong { color: var(--brand-blue); font-weight: 600; }
  .services-heading {
    position: absolute; top: 287px; left: 0; right: 0;
    font-size: 16px; font-weight: 600; letter-spacing: 0.3px;
  }
  .services-list {
    position: absolute; top: 316px; left: 0; right: 0;
    font-size: 16.5px; line-height: 24px; letter-spacing: 0.4px;
  }
</style>
</head>
<body>
  <section class="card card--front">
    <div class="wordmark">TOVEK SUBTERRA</div>
    <div class="person-name">BRENT DACOSTA</div>
    <div class="title-row"><span class="rule"></span><span class="job-title">Director of Business Development</span><span class="rule"></span></div>
    <div class="contact-row">
      <svg viewBox="0 0 20 20" aria-hidden="true"><circle cx="10" cy="10" r="10" fill="#1e7fd0"/><path d="M6 7.5c0-1 1-1.5 4-1.5s4 .5 4 1.5v1h-2v-1h-4v1H6z M7 9.5h6l1 4H6z" fill="#fff"/></svg>
      <span>(913) 555-0187</span>
      <span class="gap"></span>
      <svg viewBox="0 0 20 20" aria-hidden="true"><circle cx="10" cy="10" r="10" fill="#1e7fd0"/><rect x="5" y="6.5" width="10" height="7" fill="none" stroke="#fff" stroke-width="1.3"/><path d="M5 6.5l5 4 5-4" fill="none" stroke="#fff" stroke-width="1.3"/></svg>
      <span>brent.dacosta@tovekgrid.example</span>
    </div>
    <div class="website">www.<strong>tovekgrid</strong>.example</div>
  </section>

  <section class="card card--back">
    <div class="wordmark">TOVEK SUBTERRA</div>
    <div class="services-heading">CONSTRUCTION SERVICES INCLUDING:</div>
    <div class="services-list">
      Small Cell Construction • Boring/Drilling • Plowing / Trenching<br>
      Conduit installation • Fiber pulling • splicing • building entries<br>
      Aerial construction • Aerial Make Ready • Make Ready Engineering
    </div>
  </section>
</body>
</html>
```